Redesign Fruit Juice Label Apple&Goji make it more valuable

Need to have redesigned my label (see attached WELVARDHOF_ETK_APFELGOJI..)- please use text from the old label (including the logo bergkrongoji - SEE updated text in MUST HAVES). The colours can vary.

The new label should be
- keep it minimalistic
- hipster

The target market are luxury segments, like 5 star hotels.
The bottle will remain the same (high 162,6mm, diameter 52,1mm) - the bottle size you find under the attached "BOTTLE SIZES". Here the link to the bottle:
http://www.plumavex.com/product_info.php/cPath/5_6/products_id/249
There will be a red tap and not a gold one (see attached RED TAP).

I attached some examples of labels I like (Example 1 - 4). The size of the label on the bottle can vary as you like, also possible if divided in two parts (no problem for the labelling machine). www.bergkron-goji.example

Reason: Because of the many designs the deadline has been extended the whole week. Please make your changes, so that I can make the final decision.

Target Market(s)

5 Star Hotels, health organic markets, wellness spa

Requirements
Must have
• Logo, text and barcode - attention the text is in three languages German - Italian - English please use a delimiter symbol (I used -) to separate them (or make it visible in an other way). Plese FELIX GRAF MERTEL has also to be marked (or make it visible)
• TEXT:
• Gojibeeren - Bacche di goji - Gojiberries (Lycium barbarum)
• Die wundersame Frucht aus dem Herzen Südtirols reich an Vitalstoffen.
• Il frutto miracoloso dal cuore delle Dolomiti, ricco di sostanze vitali.
• The miracle fruit from the heart of the Dolomites, high in vital nutrients.
• apfel - mela - apple
• Goji Lycium barbarum
• 100% saft - succo - juice
• Südtirol - Alto Adige
• www.bergkron-goji.example
• Zutaten - Ingredienti - Ingredients
• Apfelsaft naturtrüb (90 %) und Gojisaft – Lycium barbarum (10 %)
• succo di mela torbido (90 %) e succo di goji – Lycium barbarum (10 %)
• unfiltered apple juice (90 %) and goji juice – Lycium barbarum (10 %)
• Hergestellt für - Prodotto per
• Welvardhof Via Roseto 17 I-39088 Egna Felix Graf Mertel
• info@bergkron-goji.example
• Non disperdere nell’ambiente (HAS TO BE AT LEAST 2MM HIGH)
• Vor Gebrauch gut schütteln - Agitare bene prima dell’apertura - shake it before opening
• 200 ml (WITH THE E AND BARCODE)
• Nach dem Öffnen im Kühlschrank aufbewahren und innerhalb weniger
• Tage verbrauchen - Da conservare in frigorifero e consumare entro
• pochi giorni - After opening store in the refrigerator and consume
• within next few days
• Mindestens haltbar bis: Da consumarsi preferibilmente entro:
• Best before: 30.06.2018
Nice to have
• I like hand paintings
Should not have
• The Label should not look cheap

```html
<!DOCTYPE html>
<html lang="en">
<head>
<meta charset="utf-8">
<title>bergkrongoji – Apfel & Goji Label</title>
<link rel="stylesheet" href="https://fonts.googleapis.com/css2?family=Amatic+SC:wght@400&family=Bebas+Neue&family=Big+Shoulders+Inline+Display:wght@500&family=Poiret+One&family=Roboto+Condensed:wght@700&display=swap">
<style>
  :root {
    --label-bg: #fdd89b;
    --cream: #fdf0c9;
    --ink: #3a3a3c;
    --berry-red: #b0262a;
  }
  html, body {
    margin: 0;
    padding: 0;
    overflow: hidden;
    background: var(--label-bg);
  }
  .label {
    position: relative;
    width: 1040px;
    height: 1200px;
    background: var(--label-bg);
    overflow: hidden;
  }
  .label-art {
    position: absolute;
    inset: 0;
  }
  .brand {
    position: absolute;
    left: 0;
    width: 1040px;
    top: 150px;
    margin: 0;
    display: flex;
    justify-content: center;
    align-items: center;
    gap: 22px;
  }
  .brand-dot {
    width: 34px;
    height: 34px;
    border-radius: 50%;
    background: var(--berry-red);
  }
  .brand-name {
    margin: 0;
    font-family: "Roboto Condensed", "Arial Narrow", sans-serif;
    font-weight: 700;
    font-size: 84px;
    letter-spacing: -2px;
    color: var(--ink);
    line-height: 1;
  }
  .variety {
    position: absolute;
    left: 0;
    width: 1040px;
    top: 410px;
    margin: 0;
    text-align: center;
    font-family: "Bebas Neue", "Oswald", sans-serif;
    font-weight: 400;
    font-size: 106px;
    letter-spacing: 2px;
    line-height: 1;
    color: var(--ink);
  }
  .variety .divider {
    color: var(--berry-red);
    padding: 0 14px;
  }
  .variety-accent {
    position: absolute;
    left: 0;
    width: 1040px;
    top: 512px;
    margin: 0;
    text-align: center;
    font-family: "Big Shoulders Inline Display", "Bebas Neue", sans-serif;
    font-weight: 500;
    font-size: 224px;
    letter-spacing: 14px;
    line-height: 1;
    color: var(--berry-red);
  }
  .botanical {
    position: absolute;
    left: 0;
    width: 1040px;
    top: 822px;
    margin: 0;
    text-align: center;
    font-family: "Poiret One", sans-serif;
    font-size: 70px;
    letter-spacing: 2px;
    line-height: 1;
    color: var(--ink);
  }
  .juice-content {
    position: absolute;
    left: 0;
    width: 1040px;
    top: 904px;
    margin: 0;
    text-align: center;
    font-family: "Poiret One", sans-serif;
    font-size: 38px;
    letter-spacing: 2px;
    word-spacing: 4px;
    line-height: 1;
    color: var(--ink);
  }
  .producer {
    position: absolute;
    left: 150px;
    width: 730px;
    top: 1040px;
    margin: 0;
    text-align: center;
    font-family: "Amatic SC", cursive;
    font-size: 104px;
    letter-spacing: 2px;
    line-height: 1;
    color: var(--ink);
  }
</style>
</head>
<body>
<main class="label">
  <svg class="label-art" width="1040" height="1200" viewBox="0 0 1040 1200" aria-hidden="true">
    <g stroke="var(--ink)" stroke-width="3" fill="none">
      <path d="M246 802 Q520 795 790 802"/>
      <circle cx="240" cy="802" r="5"/>
      <circle cx="796" cy="802" r="5"/>
      <path d="M246 972 Q520 966 790 972"/>
      <circle cx="240" cy="972" r="5"/>
      <circle cx="796" cy="972" r="5"/>
    </g>
    <path class="ribbon" d="M152 1030 L878 1030 L860 1095 L878 1160 L152 1160 L172 1095 Z"
      fill="var(--cream)" stroke="var(--ink)" stroke-width="4" stroke-linejoin="round"/>
  </svg>

  <div class="brand">
    <span class="brand-dot" aria-hidden="true"></span>
    <h1 class="brand-name">bergkrongoji</h1>
  </div>

  <h2 class="variety">APFEL<span class="divider">I</span>MELA<span class="divider">I</span>APPLE</h2>
  <p class="variety-accent">&amp; GOJI</p>

  <p class="botanical">lycium barbarum</p>
  <p class="juice-content">100 % saft &nbsp;|&nbsp; succo &nbsp;|&nbsp; juice</p>

  <p class="producer">FELIX GRAF MERTEL</p>
</main>
</body>
</html>
```